Re-design of Business Card

We require a design for our business card.

Quorin is a supplier of industrial packaging specializing in plastic products. We are undergoing a rebranding to appear more corporate. We have changed our company name to quorin and have a new logo.

I have uploaded our old card design with the previous company name.
Don't copy the current design. We are looking for a new design.

Industry/Entity Type

Manufacturing

Contact Information for Business Card

please don't copy the current design. we are looking for a new design.

Font styles to use
Sans Serif

Colors

Designer to choose colors to be used in the design.

Requirements
Must have
• clean and easy to read.

```html
<!DOCTYPE html>
<html lang="en">
<head>
<meta charset="utf-8">
<title>Quorin Business Card</title>
<link rel="stylesheet" href="https://fonts.googleapis.com/css2?family=Montserrat:wght@400;500;700&display=swap">
<style>
  :root {
    --backdrop: #2b2d30;
    --card-white: #ffffff;
    --card-dark: #46494b;
    --brand-orange: #f07a1a;
    --map-gold: #f6b52e;
    --badge-gold: #d9a126;
    --text-grey: #55585b;
    --text-light: #e4e4e4;
    --rule-grey: #8a8d90;
  }
  * { box-sizing: border-box; margin: 0; padding: 0; }
  html, body { width: 1200px; height: 900px; overflow: hidden; }
  body {
    background: var(--backdrop);
    font-family: "Montserrat", Arial, sans-serif;
    display: flex;
    align-items: center;
    justify-content: center;
    gap: 40px;
  }
  .card {
    width: 525px;
    height: 300px;
    position: relative;
    border-radius: 4px;
    overflow: hidden;
  }

  /* Front */
  .card-front { background: var(--card-white); color: var(--text-grey); }
  .brand {
    position: absolute; left: 34px; top: 30px;
    display: flex; align-items: center; gap: 10px;
  }
  .brand-mark { width: 18px; height: 18px; background: var(--brand-orange); }
  .brand-name {
    font-weight: 700; font-size: 38px; letter-spacing: 1px;
    color: var(--brand-orange); text-transform: uppercase;
  }
  .contact-list {
    position: absolute; left: 34px; top: 118px;
    list-style: none; font-size: 13px; line-height: 22px;
  }
  .contact-list li { display: flex; align-items: center; gap: 10px; }
  .contact-list svg { width: 13px; height: 13px; flex: none; }
  .contact-list .site-name { color: var(--brand-orange); font-weight: 700; }
  .holder {
    position: absolute; right: 34px; top: 150px; text-align: right;
    font-size: 13.5px; line-height: 19px;
  }
  .holder-name {
    color: var(--brand-orange); font-weight: 700; font-size: 19px;
    text-transform: uppercase; letter-spacing: .5px; line-height: 24px;
  }
  .holder-role { margin-bottom: 10px; }
  .base-rule {
    position: absolute; left: 34px; right: 34px; bottom: 30px;
    border-top: 1px solid var(--rule-grey);
  }

  /* Back */
  .card-back { background: var(--card-dark); color: var(--text-light); }
  .range-list {
    position: absolute; left: 26px; top: 24px; list-style: none;
    font-size: 11.5px; line-height: 15px;
  }
  .range-heading {
    color: var(--brand-orange); font-weight: 700; text-transform: uppercase;
    display: flex; align-items: center; gap: 6px; margin-top: 2px;
  }
  .range-heading::before {
    content: ""; width: 5px; height: 5px; background: var(--text-light);
  }
  .range-item { padding-left: 12px; }
  .range-item::before { content: "> "; }
  .credentials {
    position: absolute; right: 22px; top: 28px;
    display: flex; gap: 14px;
  }
  .credential-badge {
    width: 62px; height: 62px; border-radius: 50%;
    border: 5px solid var(--badge-gold);
  }
  .coverage-map {
    position: absolute; right: 40px; bottom: 22px;
    width: 230px; height: 170px; border-radius: 40px 60px 30px 70px;
    background: linear-gradient(160deg, #f8c04a, var(--map-gold));
  }
</style>
</head>
<body>
  <section class="card card-front">
    <div class="brand">
      <span class="brand-mark"></span>
      <span class="brand-name">Quorin</span>
    </div>
    <ul class="contact-list">
      <li><svg viewBox="0 0 12 12"><rect x="3" y="1" width="6" height="10" rx="1" fill="none" stroke="#f07a1a" stroke-width="1.3"/></svg>XXXX XXX XXX</li>
      <li><svg viewBox="0 0 12 12"><circle cx="6" cy="6" r="5" fill="none" stroke="#f07a1a" stroke-width="1.3"/><path d="M4 4l4 4" stroke="#f07a1a" stroke-width="1.3"/></svg>1300 418 207</li>
      <li><svg viewBox="0 0 12 12"><path d="M2 3.5 A5 5 0 0 1 10 3.5 L9 6 L7.5 5 Q6 4.5 4.5 5 L3 6 Z" fill="#f07a1a"/><rect x="3" y="7" width="6" height="4" fill="#f07a1a"/></svg>+61 7 3540 2917</li>
      <li><svg viewBox="0 0 12 12"><rect x="1" y="2.5" width="10" height="7" fill="none" stroke="#f07a1a" stroke-width="1.3"/><path d="M1 2.5l5 4 5-4" fill="none" stroke="#f07a1a" stroke-width="1.3"/></svg>dorian@quorin.com.au</li>
      <li><svg viewBox="0 0 12 12"><circle cx="6" cy="6" r="5" fill="none" stroke="#f07a1a" stroke-width="1.3"/><path d="M1 6h10M6 1v10" stroke="#f07a1a" stroke-width="1"/></svg>www.<span class="site-name">quorin</span>.com.au</li>
    </ul>
    <div class="holder">
      <p class="holder-name">Dorian Hale</p>
      <p class="holder-role">Machinery Sales Manager</p>
      <p>48 Marlow St</p>
      <p>Kelvin Grove, Qld</p>
      <p>4059 Australia</p>
    </div>
    <div class="base-rule"></div>
  </section>

  <section class="card card-back">
    <ul class="range-list">
      <li class="range-heading">Pallet Containment</li>
      <li class="range-item">Stretch</li>
      <li class="range-item">Heat Shrink</li>
      <li class="range-item">Pallet Hood</li>
      <li class="range-heading">Flexible Packaging</li>
      <li class="range-item">Bags &amp; Liners</li>
      <li class="range-item">Tube</li>
      <li class="range-item">Film &amp; Sheet</li>
      <li class="range-item">Printed Films (12 col)</li>
      <li class="range-item">Shrink Films</li>
      <li class="range-heading">Pallet Wrapping Machinery</li>
      <li class="range-item">Semi &amp; Fully Auto lines</li>
      <li class="range-item">Finance options</li>
      <li class="range-item">include Lease, Rent,</li>
      <li class="range-item">pay per wrap</li>
      <li class="range-heading">General Packaging</li>
    </ul>
    <div class="credentials">
      <div class="credential-badge"></div>
      <div class="credential-badge"></div>
      <div class="credential-badge"></div>
    </div>
    <div class="coverage-map" role="img" aria-label="Map of Australia and New Zealand with distribution locations"></div>
  </section>
</body>
</html>
```